依頼詳細
❏デザイン依頼
・ロゴ色/マゼンタ
・親近感・高級感・心からリラックスできる空間

☆リッチメニューのデザインの狙い
タ−ゲット層に高級感のある落ち着きでリラックスしていただける空間を提供していきたい。
そして、お客様の内面、外面のケアを安心して任せれる信頼感をつくる。

❏依頼詳細
<作成物>
■リッチメッセージ
リッチメニュー
合計2枚

〈リッチメニューの項目〉
下の段左から右へ①〜③
下の段左から右へ④〜⑤

〈リッチメニューの表示名〉
①About us   ②お店情報     ③SNS/Blog
④オンラインショップ ⑤最新情報 ⑥予約・問合せ

デザイン重視でここの表示名はデザイン的に英語の方がよければ
英語でも大丈夫です。意味がわかって
ニュアンスがあっていれば文字を短くするのも
お任せします。あくまでデザイン重視です。

〈画像はこちらから〉
↓ギガファイルリンク
https://52.sorahako-okuru.net/0925-a83c19b07d5e2f416c88a0b3d95e1c27

※こちらの作成以外に勝手に使用された場合は
著作権侵害で法的手段をとらせていただきます。
作成事例にも使用しないでください。

<サイズ>
・リッチメッセージ(1040×1040ピクセル)
・リッチメニュー(1200×810ピクセル)

<納品形式>
・ai形式(イラストレーターデータ)
・JPG
<詳細>
※添付ファイルをご確認ください。

<備考>
納品前の修正について、回数制限などありますか?
納品後の修正について、回数制限や料金などを教えて下さい。
色々なデザインでのご応募をお待ちしております!
記載項目
・元氣と綺麗になれるイメージ
・トータルビューティ−で内面から素敵な人に
サイズ
• ・リッチメッセージ(1040×1040ピクセル) ・リッチメニュー(1200×810ピクセル)
希望イメージ
シンプル 複雑
単色 カラフル
暗い 明るい
日常 高級
遊び心 厳粛
未来的 伝統的
女性的 男性的
希望する色
赤系、マゼンダ
納品ファイル
• 高解像度JPG (.jpg)
• イラストレーター形式 (.ai)
補足説明

依頼内容にぴったりで、対応も素晴らしかった。

様々な素敵な提案をありがとうございました。
今後も宜しくお願いします。

```html
<!DOCTYPE html>
<html lang="ja">
<head>
<meta charset="utf-8">
<title>Lumo Rich Menu</title>
<link href="https://fonts.googleapis.com/css2?family=Noto+Sans+JP:wght@400;500;700&family=Lato:wght@400&display=swap" rel="stylesheet">
<style>
  :root {
    --magenta: #a5145c;
    --tile: rgba(190, 38, 108, 0.72);
    --tile-edge: rgba(255, 225, 240, 0.85);
    --ink-soft: #7a6f74;
    --paper: #ffffff;
    --page: #f7f3f1;
    --wood-a: #c99a6a;
    --wood-b: #e7c9a3;
    --street-a: #b9a9a3;
    --street-b: #e9ddd6;
  }
  * { margin: 0; padding: 0; box-sizing: border-box; }
  html, body { width: 803px; height: 1200px; overflow: hidden; }
  body {
    background: var(--page);
    font-family: "Noto Sans JP", sans-serif;
    position: relative;
  }
  .menu-card {
    position: absolute; left: 48px; top: 48px; width: 707px; height: 1104px;
    background: var(--paper);
    box-shadow: 0 0 18px rgba(0,0,0,0.08);
  }
  .team-photo {
    position: absolute; left: 80px; top: 75px; width: 643px; height: 360px;
    background: linear-gradient(180deg, var(--wood-a) 0%, var(--wood-b) 70%, #ffffff 100%);
  }
  .brand {
    position: absolute; left: 80px; top: 430px; width: 643px; text-align: center;
  }
  .brand-tagline {
    font-family: "Lato", sans-serif; font-size: 22px; letter-spacing: 2px;
    color: var(--ink-soft);
  }
  .brand-name {
    font-family: "Noto Sans JP", sans-serif; font-weight: 700;
    font-size: 96px; line-height: 1.15; color: var(--magenta); margin-top: 8px;
  }
  .brand-sub {
    font-size: 17px; color: var(--ink-soft); letter-spacing: 2px; margin-top: 6px;
  }
  .shop-photo {
    position: absolute; left: 80px; top: 682px; width: 643px; height: 443px;
    background: linear-gradient(160deg, var(--street-b) 0%, var(--street-a) 100%);
  }
  .menu-grid {
    position: absolute; left: 88px; top: 700px; width: 627px;
    display: grid; grid-template-columns: repeat(3, 198px); grid-auto-rows: 200px;
    column-gap: 16px; row-gap: 16px;
  }
  .menu-tile {
    background: var(--tile); border: 2px solid var(--tile-edge); border-radius: 6px;
    display: flex; flex-direction: column; align-items: center; justify-content: center;
    color: #fff; text-align: center; padding: 0 8px;
  }
  .menu-tile svg { width: 68px; height: 68px; margin-bottom: 12px; }
  .menu-title { font-size: 18px; font-weight: 700; line-height: 1.25; white-space: nowrap; }
  .menu-en { font-family: "Lato", sans-serif; font-size: 14px; margin-top: 4px; }
</style>
</head>
<body>
  <div class="menu-card"></div>
  <div class="team-photo" role="img" aria-label="Salon team of five standing in front of a light wood wall, framed by green leaves"></div>

  <div class="brand">
    <div class="brand-tagline">Hair / Relaxation</div>
    <div class="brand-name">Lumo</div>
    <div class="brand-sub">［ヘアー・リラクゼーション ルモ］</div>
  </div>

  <div class="shop-photo" role="img" aria-label="Salon exterior and staff in soft tones behind the menu"></div>

  <nav class="menu-grid">
    <div class="menu-tile">
      <svg viewBox="0 0 68 68" fill="none" stroke="#fff" stroke-width="3">
        <path d="M34 56 C10 40 10 22 22 18 C28 16 32 20 34 24 C36 20 40 16 46 18 C58 22 58 40 34 56Z" fill="#fff"/>
        <path d="M54 6 v10 M49 11 h10" stroke-linecap="round"/>
      </svg>
      <div class="menu-title">サロン概要</div>
      <div class="menu-en">About us</div>
    </div>
    <div class="menu-tile">
      <svg viewBox="0 0 68 68" fill="none" stroke="#fff" stroke-width="3" stroke-linecap="round">
        <rect x="14" y="10" width="40" height="50" rx="4"/>
        <rect x="26" y="6" width="16" height="8" rx="2" fill="#fff"/>
        <path d="M21 26 l3 3 5-5 M33 27 h14 M21 38 l3 3 5-5 M33 39 h14 M21 50 l3 3 5-5 M33 51 h14"/>
      </svg>
      <div class="menu-title">お店情報</div>
      <div class="menu-en">Salon information</div>
    </div>
    <div class="menu-tile">
      <svg viewBox="0 0 68 68" fill="none" stroke="#fff" stroke-width="3">
        <path d="M34 10 C18 10 8 20 8 32 C8 40 13 46 20 50 L18 60 L30 53 C31 53 33 54 34 54 C50 54 60 44 60 32 C60 20 50 10 34 10Z"/>
        <circle cx="23" cy="32" r="3.5" fill="#fff"/><circle cx="34" cy="32" r="3.5" fill="#fff"/><circle cx="45" cy="32" r="3.5" fill="#fff"/>
      </svg>
      <div class="menu-title">SNS / Blog</div>
      <div class="menu-en">Social media</div>
    </div>
    <div class="menu-tile">
      <svg viewBox="0 0 68 68" fill="none" stroke="#fff" stroke-width="3" stroke-linecap="round">
        <path d="M14 22 H54 L50 60 H18 Z" fill="#fff"/>
        <path d="M25 28 V18 C25 12 29 8 34 8 C39 8 43 12 43 18 V28"/>
      </svg>
      <div class="menu-title">オンラインショップ</div>
      <div class="menu-en">Online Shop</div>
    </div>
    <div class="menu-tile">
      <svg viewBox="0 0 68 68" fill="none" stroke="#fff" stroke-width="3" stroke-linecap="round">
        <rect x="8" y="12" width="52" height="44" rx="3"/>
        <rect x="14" y="20" width="20" height="14" fill="#fff"/>
        <path d="M40 22 h14 M40 30 h14 M14 42 h40 M14 49 h40"/>
      </svg>
      <div class="menu-title">最新情報</div>
      <div class="menu-en">New information</div>
    </div>
    <div class="menu-tile">
      <svg viewBox="0 0 68 68" fill="none" stroke="#fff" stroke-width="3">
        <circle cx="34" cy="34" r="26"/>
        <path d="M24 20 l6 -2 4 9 -4 3 c2 5 5 8 10 10 l3 -4 9 4 -2 6 c-14 2 -28 -12 -26 -26z" fill="#fff" stroke-linejoin="round"/>
      </svg>
      <div class="menu-title">予約・お問い合わせ</div>
      <div class="menu-en">Contact Us</div>
    </div>
  </nav>
</body>
</html>
```